Awesome Business Card and stationary Project!
Attorney
Awesome Business Card and stationary Project! -
Creative Brief
Professional
Rosalind T. Dalwyn
Attorney at Law
5182 N. Brookfield Lane, Ste. 416 Las Vegas NV 89147
rdalwyn@rdalwynlegal.example
www.rdalwynlegal.example
Please use our logo and font...have fun Stationary and business cards: we are completey open to ideas as to where the info should be located
RTD logo on the back. At the bottom: Offices in Las Vegas, NV and San Diego, CA

```html
<!DOCTYPE html>
<html lang="en">
<head>
<meta charset="utf-8">
<title>Rosalind T. Dalwyn — Stationery Set</title>
<link href="https://fonts.googleapis.com/css2?family=Cormorant+Garamond:wght@600&family=Lato:wght@400&display=swap" rel="stylesheet">
<style>
:root{
  --backdrop:#ebe6de;
  --paper:#ffffff;
  --ink:#3a3a3a;
  --muted:#8a8a8a;
  --green:#5f7a3c;
  --green-dark:#3f5527;
  --gray:#8c8c8c;
  --gray-dark:#5e5e5e;
  --faint:#ededed;
  --shadow:0 1px 3px rgba(0,0,0,.25);
}
*{box-sizing:border-box;margin:0;padding:0}
html,body{width:1200px;height:346px;overflow:hidden}
body{background:var(--backdrop);font-family:'Lato',sans-serif;color:var(--ink);position:relative}
.piece{position:absolute;background:var(--paper);box-shadow:var(--shadow);overflow:hidden}
.caption{position:absolute;font-size:4px;letter-spacing:.4px;text-transform:uppercase;color:var(--muted);white-space:nowrap}
.signature{position:absolute;display:flex;align-items:center;gap:3px;white-space:nowrap}
.signature-square{width:6px;height:6px;background:var(--green-dark);flex:none}
.firm{font-family:'Cormorant Garamond',serif;font-weight:600;font-size:5px;color:var(--ink);line-height:1.1;white-space:nowrap}
.tiny{font-size:2.8px;line-height:1.45;color:var(--muted);white-space:nowrap}
.band{position:absolute;left:0;right:0;bottom:6px;height:5px;background:linear-gradient(90deg,var(--gray) 0%,#c4c4c4 62%,var(--green) 100%);clip-path:polygon(0 0,62% 0,66% 100%,0 100%)}
.band-right{position:absolute;right:0;bottom:6px;height:5px;width:36%;background:linear-gradient(90deg,var(--green),var(--green-dark));clip-path:polygon(8% 0,100% 0,100% 100%,0 100%)}
.watermark{position:absolute;left:0;right:0;text-align:center;font-family:'Cormorant Garamond',serif;font-weight:600;color:var(--faint);white-space:nowrap}
/* business cards */
.card{left:12px;width:132px;height:44px}
.card-front{top:125px}
.card-back{top:180px}
.card .signature{left:8px;top:7px}
.card .tiny{position:absolute;left:8px;top:24px}
.card-back .watermark{top:12px;font-size:14px}
.card-back .band,.card-back .band-right{bottom:3px;height:3px}
/* letterhead */
.sheet{top:7px;width:171px;height:322px}
.sheet-one{left:182px}
.sheet-two{left:367px}
.sheet .signature{left:12px;top:11px}
.sheet .contact{position:absolute;right:12px;top:10px;text-align:right}
.sheet-one .watermark{top:232px;font-size:20px}
.sheet-two .watermark{top:150px;font-size:20px}
.sheet .footer{position:absolute;left:0;right:0;bottom:14px;text-align:center}
/* envelope fronts */
.envelope{left:617px;width:211px;height:106px}
.env-a{top:38px}
.env-b{top:163px}
.envelope .signature{left:10px;top:9px}
.envelope .tiny{position:absolute;left:10px;top:19px}
.env-b .watermark{left:auto;right:14px;top:80px;font-size:14px}
/* envelope backs */
.env-back{left:845px;width:182px}
.back-green{top:5px;height:88px}
.back-gray{top:96px;height:86px}
.back-white{top:188px;height:100px}
.env-back svg{position:absolute;left:0;top:0}
.env-back .signature{left:0;right:0;justify-content:center;top:26px}
.env-back .light{color:#fff}
.env-back .light-square{background:#fff}
</style>
</head>
<body>

<span class="caption" style="left:12px;top:116px">Business Cards</span>

<div class="piece card card-front">
  <div class="signature"><span class="signature-square"></span><span class="firm">Rosalind T. Dalwyn, PC</span></div>
  <div class="tiny">Rosalind T. Dalwyn<br>Attorney at Law<br>rdalwyn@rdalwynlegal.example</div>
</div>
<div class="piece card card-back">
  <div class="watermark">Rosalind T. Dalwyn</div>
  <div class="band"></div><div class="band-right"></div>
</div>

<div class="piece sheet sheet-one">
  <div class="signature"><span class="signature-square"></span><span class="firm">Rosalind T. Dalwyn, PC</span></div>
  <div class="tiny contact">5182 N. Brookfield Lane, Ste. 416<br>Las Vegas NV 89147<br>rdalwyn@rdalwynlegal.example<br>www.rdalwynlegal.example</div>
  <div class="watermark">Rosalind T. Dalwyn</div>
  <div class="tiny footer">Offices in Las Vegas, NV and San Diego, CA</div>
  <div class="band"></div><div class="band-right"></div>
</div>
<span class="caption" style="left:230px;top:333px">Letterhead Page One</span>

<div class="piece sheet sheet-two">
  <div class="watermark">Rosalind T. Dalwyn</div>
  <div class="tiny footer">Offices in Las Vegas, NV and San Diego, CA</div>
  <div class="band"></div><div class="band-right"></div>
</div>
<span class="caption" style="left:415px;top:333px">Letterhead Page Two</span>

<div class="piece envelope env-a">
  <div class="signature"><span class="signature-square"></span><span class="firm">Rosalind T. Dalwyn, PC</span></div>
  <div class="tiny">5182 N. Brookfield Lane, Ste. 416<br>Las Vegas NV 89147</div>
  <div class="band" style="bottom:4px;height:3px"></div><div class="band-right" style="bottom:4px;height:3px"></div>
</div>
<span class="caption" style="left:690px;top:148px">Envelope Front Option A</span>

<div class="piece envelope env-b">
  <div class="signature"><span class="signature-square"></span><span class="firm">Rosalind T. Dalwyn, PC</span></div>
  <div class="tiny">5182 N. Brookfield Lane, Ste. 416<br>Las Vegas NV 89147</div>
  <div class="watermark">Rosalind T. Dalwyn</div>
</div>
<span class="caption" style="left:690px;top:273px">Envelope Front Option B</span>

<div class="piece env-back back-green">
  <svg width="182" height="88" viewBox="0 0 182 88"><defs><linearGradient id="flapGreen" x1="0" y1="0" x2="1" y2="0"><stop offset="0" stop-color="#4c6530"/><stop offset=".5" stop-color="#7d9658"/><stop offset="1" stop-color="#3f5527"/></linearGradient></defs><path d="M0 0H182V32L91 58 0 32Z" fill="url(#flapGreen)"/><path d="M0 88L91 50 182 88" fill="none" stroke="#e2e2e2" stroke-width=".6"/></svg>
  <div class="signature"><span class="signature-square light-square"></span><span class="firm light">Rosalind T. Dalwyn, PC</span></div>
</div>
<div class="piece env-back back-gray">
  <svg width="182" height="86" viewBox="0 0 182 86"><defs><linearGradient id="flapGray" x1="0" y1="0" x2="1" y2="0"><stop offset="0" stop-color="#5e5e5e"/><stop offset=".5" stop-color="#a6a6a6"/><stop offset="1" stop-color="#5e5e5e"/></linearGradient></defs><path d="M0 0H182V30L91 56 0 30Z" fill="url(#flapGray)"/><path d="M0 86L91 48 182 86" fill="none" stroke="#e2e2e2" stroke-width=".6"/></svg>
  <div class="signature"><span class="signature-square light-square"></span><span class="firm light">Rosalind T. Dalwyn, PC</span></div>
</div>
<div class="piece env-back back-white">
  <svg width="182" height="100" viewBox="0 0 182 100"><path d="M0 0L91 50 182 0" fill="none" stroke="#d6d6d6" stroke-width=".8"/><path d="M0 100L91 55 182 100" fill="none" stroke="#e2e2e2" stroke-width=".6"/></svg>
  <div class="signature" style="top:40px"><span class="signature-square"></span><span class="firm">Rosalind T. Dalwyn, PC</span></div>
</div>
<span class="caption" style="left:900px;top:292px">Envelope Back Options</span>

</body>
</html>
```